Fiber Arts Workshop: Business Cards & Stationery
Copper Kettle StitchHouse, LLC
Fiber Arts Workshop: Business Cards & Stationery - Hobbies
Creative Brief
Bright & Fun-filled
Marla Penrose
Principal
48 Birchwood Terrace #512 Millbrook, New Jersey 07322
marla.penrose@ckstitchhouse.example
www.ckstitchhouse.example
Fonts - you may use fonts other than those used in the logo if they enhance the design

```html
<!DOCTYPE html>
<html lang="en">
<head>
<meta charset="utf-8">
<title>Copper Kettle StitchHouse – Business Cards</title>
<link href="https://fonts.googleapis.com/css2?family=Open+Sans:wght@400;600&display=swap" rel="stylesheet">
<style>
  :root {
    --stage: #e9e6e2;
    --card: #ffffff;
    --ink: #555555;
    --ink-soft: #7a7a7a;
    --rule: #cfcfcf;
    --green: #7b9a38;
    --orange: #f29a1c;
    --purple: #6a4d9e;
    --teal: #25a39a;
  }
  * { box-sizing: border-box; margin: 0; padding: 0; }
  html, body { width: 1200px; height: 720px; overflow: hidden; }
  body {
    background: var(--stage);
    font-family: "Open Sans", Arial, sans-serif;
    color: var(--ink);
    position: relative;
  }
  .card {
    position: absolute;
    width: 540px;
    height: 300px;
    background: var(--card);
    border-radius: 18px;
    overflow: hidden;
    box-shadow: 0 2px 8px rgba(0,0,0,0.12);
  }
  .card--green  { left: 40px;  top: 40px;  --accent: var(--green); }
  .card--orange { left: 620px; top: 40px;  --accent: var(--orange); }
  .card--purple { left: 40px;  top: 380px; --accent: var(--purple); }
  .card--teal   { left: 620px; top: 380px; --accent: var(--teal); }

  .brand {
    position: absolute;
    left: 30px;
    top: 34px;
    display: flex;
    align-items: center;
    gap: 10px;
  }
  .brand__dot {
    width: 26px; height: 26px;
    border-radius: 50%;
    background: var(--accent);
  }
  .brand__name {
    font-size: 19px;
    font-weight: 400;
    color: var(--ink);
    letter-spacing: 0.2px;
  }
  .card--teal .brand__name { font-size: 24px; }
  .card--teal .brand__dot { width: 32px; height: 32px; }

  .contact {
    position: absolute;
    display: flex;
    font-size: 11px;
    line-height: 16px;
    white-space: nowrap;
  }
  .card--green .contact, .card--orange .contact { right: 40px; top: 100px; }
  .card--purple .contact { left: 40px; top: 150px; }
  .card--teal .contact { right: 40px; top: 150px; }

  .person {
    text-align: right;
    padding-right: 12px;
    border-right: 1px solid var(--rule);
    color: var(--ink-soft);
  }
  .card--purple .person { text-align: left; }
  .person__name, .person__title { color: var(--accent); }

  .reach {
    list-style: none;
    padding-left: 12px;
    color: var(--accent);
  }
  .reach li { display: flex; align-items: center; gap: 6px; }
  .reach li span { color: var(--ink-soft); }
  .reach svg { width: 12px; height: 12px; flex: none; }

  .band {
    position: absolute;
    left: 0; bottom: 0;
    width: 540px; height: 80px;
  }
</style>
</head>
<body>

<svg width="0" height="0" style="position:absolute">
  <defs>
    <symbol id="icon-phone" viewBox="0 0 12 12">
      <circle cx="6" cy="6" r="6" fill="currentColor"/>
      <path d="M4 3.2 L5 3 L5.5 4.6 L4.9 5.1 Q5.6 6.5 6.9 7.1 L7.4 6.5 L9 7 L8.8 8 Q8.5 8.8 7.5 8.7 Q4 8 3.3 4.5 Q3.2 3.5 4 3.2 Z" fill="#fff"/>
    </symbol>
    <symbol id="icon-mail" viewBox="0 0 12 12">
      <circle cx="6" cy="6" r="6" fill="currentColor"/>
      <rect x="3" y="4" width="6" height="4.2" fill="#fff"/>
      <path d="M3 4 L6 6.4 L9 4" fill="none" stroke="currentColor" stroke-width="0.7"/>
    </symbol>
    <symbol id="icon-web" viewBox="0 0 12 12">
      <circle cx="6" cy="6" r="6" fill="currentColor"/>
      <circle cx="6" cy="6" r="3.2" fill="none" stroke="#fff" stroke-width="0.8"/>
      <path d="M2.8 6 H9.2 M6 2.8 Q4.3 6 6 9.2 M6 2.8 Q7.7 6 6 9.2" fill="none" stroke="#fff" stroke-width="0.6"/>
    </symbol>
  </defs>
</svg>

<section class="card card--green">
  <div class="brand"><span class="brand__dot"></span><span class="brand__name">Copper Kettle StitchHouse</span></div>
  <div class="contact">
    <div class="person">
      <div class="person__name">Marla Penrose</div>
      <div class="person__title">Principal</div>
      <div>48 Birchwood Terrace #512</div>
      <div>Millbrook, New Jersey 07322</div>
    </div>
    <ul class="reach">
      <li><svg><use href="#icon-phone"/></svg><span>(555) 014-2290</span></li>
      <li><svg><use href="#icon-mail"/></svg><span>marla.penrose@ckstitchhouse.example</span></li>
      <li><svg><use href="#icon-web"/></svg><span>www.ckstitchhouse.example</span></li>
    </ul>
  </div>
  <svg class="band" viewBox="0 0 540 80" preserveAspectRatio="none">
    <path d="M0 34 Q270 -6 540 34" fill="none" stroke="var(--green)" stroke-opacity="0.35" stroke-width="2"/>
    <path d="M0 44 Q270 4 540 44 L540 80 L0 80 Z" fill="var(--green)"/>
  </svg>
</section>

<section class="card card--orange">
  <div class="brand"><span class="brand__dot"></span><span class="brand__name">Copper Kettle StitchHouse</span></div>
  <div class="contact">
    <div class="person">
      <div class="person__name">Marla Penrose</div>
      <div class="person__title">Principal</div>
      <div>48 Birchwood Terrace #512</div>
      <div>Millbrook, New Jersey 07322</div>
    </div>
    <ul class="reach">
      <li><svg><use href="#icon-phone"/></svg><span>(555) 014-2290</span></li>
      <li><svg><use href="#icon-mail"/></svg><span>marla.penrose@ckstitchhouse.example</span></li>
      <li><svg><use href="#icon-web"/></svg><span>www.ckstitchhouse.example</span></li>
    </ul>
  </div>
  <svg class="band" viewBox="0 0 540 80" preserveAspectRatio="none">
    <path d="M0 34 Q270 -6 540 34" fill="none" stroke="var(--orange)" stroke-opacity="0.35" stroke-width="2"/>
    <path d="M0 44 Q270 4 540 44 L540 80 L0 80 Z" fill="var(--orange)"/>
  </svg>
</section>

<section class="card card--purple">
  <div class="brand"><span class="brand__dot"></span><span class="brand__name">Copper Kettle StitchHouse</span></div>
  <div class="contact">
    <div class="person">
      <div class="person__name">Marla Penrose</div>
      <div class="person__title">Principal</div>
      <div>48 Birchwood Terrace #512</div>
      <div>Millbrook, New Jersey 07322</div>
    </div>
    <ul class="reach">
      <li><svg><use href="#icon-phone"/></svg><span>(555) 014-2290</span></li>
      <li><svg><use href="#icon-mail"/></svg><span>marla.penrose@ckstitchhouse.example</span></li>
      <li><svg><use href="#icon-web"/></svg><span>www.ckstitchhouse.example</span></li>
    </ul>
  </div>
  <svg class="band" viewBox="0 0 540 80" preserveAspectRatio="none">
    <path d="M0 34 Q270 -6 540 34" fill="none" stroke="var(--purple)" stroke-opacity="0.35" stroke-width="2"/>
    <path d="M0 44 Q270 4 540 44 L540 80 L0 80 Z" fill="var(--purple)"/>
  </svg>
</section>

<section class="card card--teal">
  <div class="brand"><span class="brand__dot"></span><span class="brand__name">Copper Kettle StitchHouse</span></div>
  <div class="contact">
    <div class="person">
      <div class="person__name">Marla Penrose</div>
      <div class="person__title">Principal</div>
      <div>48 Birchwood Terrace #512</div>
      <div>Millbrook, New Jersey 07322</div>
    </div>
    <ul class="reach">
      <li><svg><use href="#icon-phone"/></svg><span>(555) 014-2290</span></li>
      <li><svg><use href="#icon-mail"/></svg><span>marla.penrose@ckstitchhouse.example</span></li>
      <li><svg><use href="#icon-web"/></svg><span>www.ckstitchhouse.example</span></li>
    </ul>
  </div>
  <svg class="band" viewBox="0 0 540 80" preserveAspectRatio="none">
    <path d="M0 34 Q270 -6 540 34" fill="none" stroke="var(--teal)" stroke-opacity="0.35" stroke-width="2"/>
    <path d="M0 44 Q270 4 540 44 L540 80 L0 80 Z" fill="var(--teal)"/>
  </svg>
</section>

</body>
</html>
```